New modern business card design

To design a brand new business card that's clean & modern in terms of layout.
I have attached our company logo and also basic information regarding what is needed on the card that also needs to be editable.

Target Market(s)

motor trade

Contact Information for Business Card

logo, name, title, tel, mob, email, address, www, all information is in the word.doc file

Requirements
Must have
• white background
Nice to have
• Nice clean font

```html
<!DOCTYPE html>
<html lang="en">
<head>
<meta charset="utf-8">
<title>Bolt Release Ltd Business Card</title>
<link rel="stylesheet" href="https://fonts.googleapis.com/css2?family=Jost:wght@600&family=Montserrat:wght@400&family=Lato:wght@400;700&display=swap">
<style>
  :root {
    --page-bg: #d6d6d6;
    --card-bg: #ffffff;
    --brand-blue: #1d61b0;
    --name-blue: #1659a8;
    --text-grey: #444444;
    --divider: #ececec;
  }
  * { margin: 0; padding: 0; box-sizing: border-box; }
  html, body {
    width: 1200px;
    height: 1200px;
    overflow: hidden;
    background: var(--page-bg);
  }
  .business-card {
    position: absolute;
    left: 220px;
    top: 372px;
    width: 761px;
    height: 457px;
    background: var(--card-bg);
  }
  .brand {
    position: absolute;
    left: 0;
    width: 354px;
    top: 0;
    height: 457px;
    display: flex;
    align-items: center;
    justify-content: center;
    gap: 12px;
  }
  .brand-mark {
    width: 26px;
    height: 26px;
    background: var(--brand-blue);
  }
  .brand-name {
    font-family: "Lato", sans-serif;
    font-weight: 700;
    font-size: 26px;
    letter-spacing: 1px;
    color: var(--brand-blue);
  }
  .divider {
    position: absolute;
    left: 354px;
    top: 56px;
    width: 2px;
    height: 344px;
    background: linear-gradient(to bottom, transparent, var(--divider) 15%, var(--divider) 85%, transparent);
  }
  .details {
    position: absolute;
    left: 404px;
    top: 0;
    right: 20px;
  }
  .person-name {
    position: absolute;
    top: 52px;
    font-family: "Jost", sans-serif;
    font-weight: 600;
    font-size: 44px;
    line-height: 1;
    color: var(--name-blue);
    white-space: nowrap;
  }
  .person-title {
    position: absolute;
    top: 100px;
    font-family: "Montserrat", sans-serif;
    font-size: 19px;
    color: var(--text-grey);
    white-space: nowrap;
  }
  .address {
    position: absolute;
    top: 149px;
    font-family: "Lato", sans-serif;
    font-style: normal;
    font-size: 21px;
    line-height: 30px;
    color: var(--text-grey);
  }
  .contact-list {
    position: absolute;
    top: 262px;
    list-style: none;
    font-family: "Lato", sans-serif;
    font-size: 21px;
    color: var(--text-grey);
  }
  .contact-item {
    position: relative;
    height: 34px;
    display: flex;
    align-items: center;
    white-space: nowrap;
  }
  .contact-icon {
    width: 20px;
    height: 20px;
    margin-left: -2px;
    margin-right: 14px;
    fill: none;
    stroke: var(--brand-blue);
    stroke-width: 1.8;
  }
  .contact-icon.solid { fill: var(--brand-blue); stroke: none; }
</style>
</head>
<body>
  <section class="business-card">
    <div class="brand">
      <span class="brand-mark"></span>
      <span class="brand-name">BOLT RELEASE LTD</span>
    </div>
    <div class="divider"></div>
    <div class="details">
      <h1 class="person-name">Daniel Marsh</h1>
      <p class="person-title">General Manager</p>
      <address class="address">
        Linden Road<br>
        Ashbury, Northfield<br>
        NF12 3QT
      </address>
      <ul class="contact-list">
        <li class="contact-item">
          <svg class="contact-icon solid" viewBox="0 0 24 24"><path d="M6.6 10.8a15 15 0 0 0 6.6 6.6l2.2-2.2a1 1 0 0 1 1-.25 11.4 11.4 0 0 0 3.6.57 1 1 0 0 1 1 1V20a1 1 0 0 1-1 1A17 17 0 0 1 3 4a1 1 0 0 1 1-1h3.5a1 1 0 0 1 1 1c0 1.25.2 2.45.57 3.57a1 1 0 0 1-.25 1z"/></svg>
          0123 450 7788
        </li>
        <li class="contact-item">
          <svg class="contact-icon" viewBox="0 0 24 24"><rect x="6" y="2" width="12" height="20" rx="2"/><line x1="10" y1="18.5" x2="14" y2="18.5"/></svg>
          07000 123 456
        </li>
        <li class="contact-item">
          <svg class="contact-icon solid" viewBox="0 0 24 24"><path d="M2 6h20v1.2l-10 6.3L2 7.2z"/><path d="M2 9.4l10 6.3 10-6.3V19H2z"/></svg>
          dmarsh@bolt-release.co.uk
        </li>
        <li class="contact-item">
          <svg class="contact-icon" viewBox="0 0 24 24" style="stroke-width:1.2"><circle cx="12" cy="12" r="10"/><ellipse cx="12" cy="12" rx="4.5" ry="10"/><line x1="2" y1="12" x2="22" y2="12"/><path d="M4 6.5h16M4 17.5h16"/></svg>
          www.bolt-release.co.uk
        </li>
      </ul>
    </div>
  </section>
</body>
</html>
```